Tallbrook Meridian Advisory needs business cards

Tallbrook Meridian Advisory is a new approach to consulting: we believe in partnering our clients in a hands-on, side-by-side, rolling-up-our sleeves approach, rather than being removed and aloof consultants.

We have a logo design developped through PixelHarbor (see attachment) and need to move to the stage of designing a business card for our 7 founding members.

Target Market(s)

Senior executives in local and global companies (such as Fizzmont Tonic, Hollanby, Brevard, etc)

Industry/Entity Type

Business

Requirements
Must have
• Look and feel: The design reflect the logo: i.e. professional, modern and approachable (as opposed to corporate traditional and remote). We are looking for a high quality, premium design.

Content must haves:
- prominent: our logo, person's name, function, phone number and e-mail address
- less prominent: company address and website

Example: Tallbrook Meridian Advisory logo, Mireille Vostag, Partner, +44 (0)781 209 3375, mireille_vostag@tallbrookmeridian.example / 17 Pelham Crescent, Esher, Surrey, UK, KT10 3WN - www.tallbrookmeridian.example

- Both sides of the card can be used
- Both versions of the logo can be used (on black or on white)

```html
<!DOCTYPE html>
<html lang="en">
<head>
<meta charset="utf-8">
<title>Tallbrook Meridian Advisory – Business Card</title>
<link rel="stylesheet" href="https://fonts.googleapis.com/css2?family=Carlito:wght@400&display=swap">
<style>
  :root {
    --backdrop: #000000;
    --card: #ffffff;
    --ink: #111111;
    --brand-ink: #333333;
    --brand-blue: #2fb4e6;
    --band-start: #3ba7d0;
    --band-end: #80d2e6;
  }
  * { margin: 0; padding: 0; box-sizing: border-box; }
  html, body {
    width: 1200px;
    height: 866px;
    overflow: hidden;
    background: var(--backdrop);
    font-family: "Carlito", "Calibri", sans-serif;
  }
  .canvas { position: relative; width: 1200px; height: 866px; }
  .card {
    position: absolute;
    left: 118px;
    top: 155px;
    width: 966px;
    height: 500px;
    background: var(--card);
  }
  .card-band {
    position: absolute;
    left: 116px;
    top: 655px;
    width: 968px;
    height: 56px;
    background: linear-gradient(90deg, var(--band-start), var(--band-end));
  }
  .text { position: absolute; color: var(--ink); font-size: 25px; line-height: 36px; white-space: nowrap; }
  .identity { left: 57px; top: 70px; }
  .phone { right: 66px; top: 74px; text-align: right; }
  .brand { position: absolute; left: 275px; top: 211px; display: flex; align-items: center; gap: 16px; }
  .brand-mark { width: 110px; height: 110px; display: block; }
  .brand-name { font-size: 30px; color: var(--brand-ink); white-space: nowrap; margin-top: 40px; }
  .contact { left: 401px; top: 333px; font-size: 24px; }
</style>
</head>
<body>
  <div class="canvas">
    <div class="card">
      <div class="text identity">Mireille Vostag,<br>Partner</div>
      <div class="text phone">+44 (0)781 209 3375,</div>
      <div class="brand">
        <svg class="brand-mark" viewBox="0 0 110 110" aria-hidden="true">
          <circle cx="55" cy="55" r="55" fill="var(--brand-blue)"/>
        </svg>
        <div class="brand-name">Tallbrook Meridian Advisory</div>
      </div>
      <div class="text contact">
        Pelham Crescent, Esher, Surrey,<br>
        mireille_vostag@tallbrookmeridian.example / 17<br>
        UK, KT10 3WN - www.tallbrookmeridian.example
      </div>
    </div>
    <div class="card-band"></div>
  </div>
</body>
</html>
```